Creative lead conversion landing page for SMBs

We have an AI chatbot webpage for a real estate agent, and we’re are going to start sending traffic to that webpage (primarily from Zintavo)
We want to maximize the percentage of visitors who start conversations with the chatbot.
We have a specific area of the webpage where we can include any HTML.
We need the design and HTML for both desktop and mobile version.
We’re looking for the best designs that help convert visitors into people who engage the chatbot.

Details are in the attached document "Pitchforge project for chat conversion". Please let me know if you have any questions!

Target Market(s)

SMBs (think real estate agents, or home services like tree care, housekeepers, electricians, general contractors) will be selling to consumers

Number of Pages Required

1 page

Font styles to use
Other font styles liked:
• Zintavo Poppins

Requirements
Must have
• Creative design that catches users eyes and with good content (content of course out of scope) will encourage a user to want to learn more.

```html
<!DOCTYPE html>
<html lang="en">
<head>
<meta charset="UTF-8">
<title>Marissa – Real Estate Agent</title>
<link href="https://fonts.googleapis.com/css2?family=Poppins:wght@400;500;600;700&display=swap" rel="stylesheet">
<style>
:root{
  --canvas:#e7e7e9;
  --white:#ffffff;
  --panel:#f2f2f3;
  --ink:#2b2b2b;
  --body:#4a4a4a;
  --muted:#8a8a8a;
  --teal:#17a6bd;
  --purple:#6a56a9;
  --gold:#f5c518;
  --navy:#0f1d30;
  --footnote:#8793a4;
}
*{box-sizing:border-box;margin:0;padding:0}
html,body{width:1200px;height:3772px;overflow:hidden}
body{background:var(--canvas);font-family:'Poppins',sans-serif;color:var(--ink)}
.page{width:756px;height:3772px;margin:0 auto;background:var(--white);display:flex;flex-direction:column}

/* header */
.agent-header{height:528px;flex:0 0 528px;position:relative;background:var(--white)}
.agent-avatar{position:absolute;left:38px;top:215px;width:214px;height:214px;border-radius:50%;border:7px solid var(--teal);padding:6px;background:var(--white)}
.agent-avatar .photo{width:100%;height:100%;border-radius:50%;background:linear-gradient(160deg,#7a5a48,#c9a48e 60%,#e8d6c8)}
.agent-name{position:absolute;left:300px;top:238px;font-size:58px;font-weight:500;line-height:1}
.agent-role{position:absolute;left:300px;top:318px;font-size:30px;color:var(--body)}
.agent-cta{position:absolute;left:300px;top:370px;font-size:27px;color:var(--teal)}
.header-chevron{position:absolute;left:50%;top:450px;transform:translateX(-50%)}

/* profile panel */
.profile-panel{height:2210px;flex:0 0 2210px;background:var(--panel);margin:0 8px;border-radius:0 0 44px 44px;padding:42px 18px 0}
.card{background:var(--white);border-radius:30px;box-shadow:0 4px 18px rgba(0,0,0,.06)}
.bio-card{height:600px;padding:36px 38px}
.section-title{font-size:44px;font-weight:500;color:var(--ink);line-height:1.2}
.bio-text{margin-top:30px;font-size:22.5px;line-height:34px;text-align:justify;color:var(--body)}
.contact-buttons{display:flex;gap:28px;margin-top:28px}
.pill{flex:1;height:64px;border-radius:32px;color:var(--white);font-size:24px;font-weight:600;display:flex;align-items:center;justify-content:center;gap:12px}
.pill-phone{background:var(--teal)}
.pill-site{background:var(--purple)}

.reviews{padding:70px 20px 0}
.review-card{padding:30px 34px;margin-top:30px}
.review-card.first{height:370px}
.review-card.second{height:516px;margin-top:54px}
.reviewer{display:flex;align-items:center;gap:22px}
.reviewer-initial{width:62px;height:62px;border-radius:50%;background:var(--purple);color:var(--white);font-size:28px;font-weight:500;display:flex;align-items:center;justify-content:center}
.reviewer-name{font-size:32px;font-weight:500}
.stars{display:flex;gap:6px;margin:16px 0 0 84px}
.review-text{margin:22px 0 0 84px;font-size:22.5px;line-height:34px;text-align:justify;color:var(--body)}

.gallery{padding:60px 20px 0}
.gallery-head{display:flex;justify-content:space-between;align-items:center}
.gallery-arrows{display:flex;gap:12px}
.gallery-arrow{width:50px;height:50px;border-radius:50%;background:#c9c9cc;display:flex;align-items:center;justify-content:center}
.gallery-track{display:flex;gap:30px;margin-top:44px;overflow:hidden;width:676px}
.gallery-photo{flex:0 0 232px;height:228px}
.photo-a{background:linear-gradient(135deg,#8a6a4e,#cdb392)}
.photo-b{background:linear-gradient(135deg,#3d3a3c,#b58d6a)}
.photo-c{background:linear-gradient(135deg,#cfd3d6,#8f979c)}

/* chat */
.chat-area{flex:1 1 auto;position:relative;background:var(--white)}
.chat-bubble{position:absolute;left:12px;top:158px;width:502px;padding:26px 30px;background:var(--white);border-radius:28px;box-shadow:0 6px 22px rgba(0,0,0,.12);font-size:29px;line-height:39px;color:var(--ink)}
.chat-bubble .hl{color:var(--teal)}
.assistant-mascot{position:absolute;left:22px;top:466px;width:96px;height:108px;border-radius:50% 50% 44% 44%;background:linear-gradient(180deg,#63c9de,#1f9fb8)}
.chat-input{position:absolute;left:12px;top:596px;width:720px;height:100px;border-radius:22px;background:#e6e6e8;padding:0 30px;display:flex;align-items:center;font-size:28px;color:var(--muted)}

/* footer */
.brand-footer{height:185px;flex:0 0 185px;background:var(--navy);display:flex;align-items:center;justify-content:space-between;padding:0 36px 0 30px}
.create-button{width:298px;height:108px;border-radius:18px;background:var(--teal);color:var(--white);font-size:27px;line-height:36px;font-weight:500;display:flex;align-items:center;padding-left:26px}
.brand-block{text-align:right}
.brand-name{font-size:46px;font-weight:600;color:var(--white);line-height:1}
.brand-note{margin-top:12px;font-size:18px;color:var(--footnote);line-height:24px}
</style>
</head>
<body>
<main class="page">
  <header class="agent-header">
    <div class="agent-avatar"><div class="photo" role="img" aria-label="Portrait photo of the agent"></div></div>
    <h1 class="agent-name">Marissa</h1>
    <p class="agent-role">Real Estate Agent</p>
    <p class="agent-cta">Talk to Perchly, my AI assistant.</p>
    <svg class="header-chevron" width="40" height="26" viewBox="0 0 40 26"><path d="M4 4 L20 20 L36 4" fill="none" stroke="#2b2b2b" stroke-width="6" stroke-linecap="round" stroke-linejoin="round"/></svg>
  </header>

  <section class="profile-panel">
    <article class="card bio-card">
      <h2 class="section-title">My Bio</h2>
      <p class="bio-text">Hi! I am Marissa. Buying or Selling a home is a big decision and can be overwhelming. That is where I come in! If you are looking to sell or buy a new home or both, I am ready to help you. Real Estate is my passion and I love helping others.I have lived in Fishers for over 15 years, with my husband and two children. When I am not helping others with their real estate needs, I enjoy spending time with my family and traveling.</p>
      <div class="contact-buttons">
        <div class="pill pill-phone">
          <svg width="22" height="22" viewBox="0 0 24 24"><path fill="#fff" d="M6.6 10.8a15 15 0 0 0 6.6 6.6l2.2-2.2c.3-.3.7-.4 1-.2 1.1.4 2.3.6 3.6.6.6 0 1 .4 1 1V20c0 .6-.4 1-1 1A17 17 0 0 1 3 4c0-.6.4-1 1-1h3.5c.6 0 1 .4 1 1 0 1.3.2 2.5.6 3.6.1.3 0 .7-.2 1z"/></svg>
          (317) 555-0182
        </div>
        <div class="pill pill-site">
          <svg width="22" height="22" viewBox="0 0 24 24"><circle cx="12" cy="12" r="10" fill="none" stroke="#fff" stroke-width="2.4"/><path d="M2 12h20M12 2c3 3 3 17 0 20M12 2c-3 3-3 17 0 20" fill="none" stroke="#fff" stroke-width="2"/></svg>
          My Website
        </div>
      </div>
    </article>

    <section class="reviews">
      <h2 class="section-title">My Reviews</h2>
      <article class="card review-card first">
        <div class="reviewer"><span class="reviewer-initial">D</span><span class="reviewer-name">Daniel and Sophie</span></div>
        <div class="stars">
          <svg width="22" height="22" viewBox="0 0 24 24"><path fill="#f5c518" d="M12 2l3 7 7.5.6-5.7 5 1.8 7.4L12 18l-6.6 4 1.8-7.4-5.7-5L9 9z"/></svg>
          <svg width="22" height="22" viewBox="0 0 24 24"><path fill="#f5c518" d="M12 2l3 7 7.5.6-5.7 5 1.8 7.4L12 18l-6.6 4 1.8-7.4-5.7-5L9 9z"/></svg>
          <svg width="22" height="22" viewBox="0 0 24 24"><path fill="#f5c518" d="M12 2l3 7 7.5.6-5.7 5 1.8 7.4L12 18l-6.6 4 1.8-7.4-5.7-5L9 9z"/></svg>
          <svg width="22" height="22" viewBox="0 0 24 24"><path fill="#f5c518" d="M12 2l3 7 7.5.6-5.7 5 1.8 7.4L12 18l-6.6 4 1.8-7.4-5.7-5L9 9z"/></svg>
          <svg width="22" height="22" viewBox="0 0 24 24"><path fill="#f5c518" d="M12 2l3 7 7.5.6-5.7 5 1.8 7.4L12 18l-6.6 4 1.8-7.4-5.7-5L9 9z"/></svg>
        </div>
        <p class="review-text">Marissa is the best! She was extremely helpful to me and my girlfriend as First-Time Home Buyers. She made the whole process super easy and stress free :)</p>
      </article>
      <article class="card review-card second">
        <div class="reviewer"><span class="reviewer-initial">J</span><span class="reviewer-name">Joanna Kemp</span></div>
        <div class="stars">
          <svg width="22" height="22" viewBox="0 0 24 24"><path fill="#f5c518" d="M12 2l3 7 7.5.6-5.7 5 1.8 7.4L12 18l-6.6 4 1.8-7.4-5.7-5L9 9z"/></svg>
          <svg width="22" height="22" viewBox="0 0 24 24"><path fill="#f5c518" d="M12 2l3 7 7.5.6-5.7 5 1.8 7.4L12 18l-6.6 4 1.8-7.4-5.7-5L9 9z"/></svg>
          <svg width="22" height="22" viewBox="0 0 24 24"><path fill="#f5c518" d="M12 2l3 7 7.5.6-5.7 5 1.8 7.4L12 18l-6.6 4 1.8-7.4-5.7-5L9 9z"/></svg>
          <svg width="22" height="22" viewBox="0 0 24 24"><path fill="#f5c518" d="M12 2l3 7 7.5.6-5.7 5 1.8 7.4L12 18l-6.6 4 1.8-7.4-5.7-5L9 9z"/></svg>
          <svg width="22" height="22" viewBox="0 0 24 24"><path fill="#f5c518" d="M12 2l3 7 7.5.6-5.7 5 1.8 7.4L12 18l-6.6 4 1.8-7.4-5.7-5L9 9z"/></svg>
        </div>
        <p class="review-text">Marissa was incredible! Your first-time home-buying experience can be intimidating, but she was with us each step of the way to thoroughly explain the process. She wanted to find a house that was the right fit for us and listened to our needs. I'd recommend working with Marissa to anyone!</p>
      </article>
    </section>

    <section class="gallery">
      <div class="gallery-head">
        <h2 class="section-title">Related Pictures</h2>
        <div class="gallery-arrows">
          <span class="gallery-arrow"><svg width="18" height="18" viewBox="0 0 18 18"><path d="M11 3 L5 9 L11 15" fill="none" stroke="#fff" stroke-width="3" stroke-linecap="round"/></svg></span>
          <span class="gallery-arrow"><svg width="18" height="18" viewBox="0 0 18 18"><path d="M7 3 L13 9 L7 15" fill="none" stroke="#fff" stroke-width="3" stroke-linecap="round"/></svg></span>
        </div>
      </div>
      <div class="gallery-track">
        <div class="gallery-photo photo-a" role="img" aria-label="Magnifying glass over a small model house"></div>
        <div class="gallery-photo photo-b" role="img" aria-label="Couple reviewing home paperwork at a table"></div>
        <div class="gallery-photo photo-c" role="img" aria-label="Agent meeting clients in a bright office"></div>
      </div>
    </section>
  </section>

  <section class="chat-area">
    <p class="chat-bubble">Hi! I'm the AI assistant to Marissa, who <span class="hl">can help you buy</span> or <span class="hl">sell a</span> home in the Indianapolis area. I am <span class="hl">happy</span> to help get you connected to her. First, what's your name?</p>
    <div class="assistant-mascot" role="img" aria-label="Small bird mascot of the chat assistant"></div>
    <div class="chat-input">Type your response...</div>
  </section>

  <footer class="brand-footer">
    <div class="create-button">Create your own<br>free Perchly</div>
    <div class="brand-block">
      <div class="brand-name">Perchly</div>
      <p class="brand-note">Perchly uses AI and can make<br>mistakes</p>
    </div>
  </footer>
</main>
</body>
</html>
```